I will ask the design of the business card

We are looking for business card design of the new company "TORVIK QUANTA WORKS LLC." Based in Azerbaijan.
In case
We are working on Azerbaijan to set up the first exchange of crypto currencies.

The key currency used in exchanges is called "MELDA".
In case
We are doing project to make crypto currency infrastructure.

We provide state-of-the-art technology to the world.

```html
<!DOCTYPE html>
<html lang="en">
<head>
<meta charset="utf-8">
<title>Torvik Quanta Works LLC – Business Card</title>
<link rel="stylesheet" href="https://fonts.googleapis.com/css2?family=Oswald:wght@500;600&family=Open+Sans:wght@400;600;700&display=swap">
<style>
  :root {
    --brand-blue: #1f4a86;
    --brand-navy: #15305c;
    --deep-navy: #0f2546;
    --ink: #2b2b2b;
    --rule-grey: #9a9a9a;
    --paper: #ffffff;
    --stage: #e9e6e1;
    --ghost: rgba(190, 205, 230, 0.22);
  }
  * { box-sizing: border-box; margin: 0; padding: 0; }
  html, body { width: 1200px; height: 1024px; overflow: hidden; }
  body {
    background: var(--stage);
    display: flex;
    flex-direction: column;
    align-items: center;
    justify-content: center;
    gap: 44px;
    font-family: "Open Sans", Arial, sans-serif;
  }
  .card {
    position: relative;
    width: 800px;
    height: 457px;
    overflow: hidden;
    box-shadow: 0 6px 18px rgba(0,0,0,0.18);
  }

  /* ---------- front ---------- */
  .card-front { background: var(--paper); }
  .card-front .edge-stripe {
    position: absolute; left: 0; right: 0; bottom: 0; height: 14px;
    background: var(--brand-blue);
  }
  .company-band {
    position: absolute; left: 52px; top: 84px;
    width: 500px; height: 74px;
    background: var(--brand-blue);
    display: flex; align-items: center; justify-content: center;
  }
  .company-band .company-name {
    font-family: "Oswald", "Arial Narrow", sans-serif;
    font-weight: 600;
    font-size: 40px;
    letter-spacing: 1px;
    color: var(--paper);
    white-space: nowrap;
  }
  .divider-thin {
    position: absolute; left: 552px; right: 40px; top: 196px;
    height: 1px; background: var(--rule-grey);
  }
  .divider-bold {
    position: absolute; left: 300px; top: 193px;
    width: 252px; height: 7px; background: var(--brand-blue);
  }
  .person {
    position: absolute; left: 58px; top: 176px;
  }
  .person .person-name {
    font-weight: 700; font-size: 25px; color: var(--brand-blue);
    letter-spacing: 0.5px;
  }
  .person .job-title {
    font-weight: 400; font-size: 19px; color: var(--ink);
    letter-spacing: 0.5px; margin-top: 2px;
  }
  .contact-list {
    position: absolute; left: 58px; top: 266px;
    list-style: none;
  }
  .contact-list li {
    display: flex; align-items: center; gap: 12px;
    font-size: 18px; color: var(--ink); line-height: 32px;
  }
  .contact-list svg { width: 18px; height: 18px; fill: var(--brand-navy); }
  .office-address {
    position: absolute; left: 520px; top: 232px;
    font-size: 18px; color: var(--ink); line-height: 28px;
  }

  /* ---------- back ---------- */
  .card-back { background: var(--deep-navy); }
  .back-texture {
    position: absolute; inset: 0;
    background: radial-gradient(circle at 45% 50%, #3a5f96 0%, #24467a 35%, #15305c 70%, #0f2546 100%);
  }
  .coin-mark {
    position: absolute; left: 0; right: 0; top: 96px;
    text-align: center;
    font-family: "Oswald", "Arial Narrow", sans-serif;
    font-weight: 500; font-size: 78px; letter-spacing: 14px;
    color: var(--ghost);
  }
  .back-company {
    position: absolute; left: 0; right: 0; top: 170px;
    text-align: center;
    font-family: "Oswald", "Arial Narrow", sans-serif;
    font-weight: 600; font-size: 54px; letter-spacing: 1.5px;
    color: var(--paper);
  }
  .coin-tagline {
    position: absolute; left: 0; right: 0; top: 250px;
    text-align: center;
    font-family: "Oswald", "Arial Narrow", sans-serif;
    font-weight: 500; font-size: 40px; letter-spacing: 16px;
    color: var(--ghost);
  }
  .back-web {
    position: absolute; left: 96px; top: 330px;
    font-size: 17px; color: var(--paper);
  }
</style>
</head>
<body>

  <section class="card card-front" aria-label="Business card front">
    <div class="company-band"><span class="company-name">TORVIK QUANTA WORKS LLC</span></div>
    <div class="divider-bold"></div>
    <div class="divider-thin"></div>

    <div class="person">
      <p class="person-name">RASIM TALEN</p>
      <p class="job-title">JOB TITLE</p>
    </div>

    <ul class="contact-list">
      <li>
        <svg viewBox="0 0 24 24" aria-hidden="true"><path d="M6.6 10.8a15.1 15.1 0 0 0 6.6 6.6l2.2-2.2a1 1 0 0 1 1-.25 11.4 11.4 0 0 0 3.6.57 1 1 0 0 1 1 1V20a1 1 0 0 1-1 1A17 17 0 0 1 3 4a1 1 0 0 1 1-1h3.5a1 1 0 0 1 1 1c0 1.25.2 2.45.57 3.57a1 1 0 0 1-.25 1z"/></svg>
        4820 1135
      </li>
      <li>
        <svg viewBox="0 0 24 24" aria-hidden="true"><path d="M2 5h20v14H2z M4 7v.5l8 5 8-5V7l-8 5z" fill-rule="evenodd"/></svg>
        rtalen@torvikquanta.com
      </li>
      <li>
        <svg viewBox="0 0 24 24" aria-hidden="true"><circle cx="12" cy="12" r="10"/><path d="M2 12h20M12 2c3 3 3 17 0 20M12 2c-3 3-3 17 0 20" stroke="#fff" stroke-width="1.4" fill="none"/></svg>
        www.torvikquanta.com
      </li>
    </ul>

    <address class="office-address" style="font-style: normal;">
      Level 4, 18 Neftchiler Avenue<br>
      SABAIL BAKU AZ1000
    </address>

    <div class="edge-stripe"></div>
  </section>

  <section class="card card-back" aria-label="Business card back">
    <div class="back-texture" role="img" aria-label="Blue geometric network mesh pattern radiating from a central coin shape"></div>
    <p class="coin-mark">MELDA</p>
    <h1 class="back-company">TORVIK QUANTA WORKS LLC</h1>
    <p class="coin-tagline">THE DIGITAL COIN</p>
    <p class="back-web">www.torvikquanta.com</p>
  </section>

</body>
</html>
```